zumoKet - website to pay membership association fee

The main purpose of this site it to allow a pre-registered user to be able to view the membership fees for their membership association and pay the same in one of the ways offered by the portal.
You are required to create a graphical project only for the logon functions as a user, while omitting the back end/administration ones that will be decided later
The site, besides being responsive must be very intuitive in its function. The graphics must be bright.

Number of Pages Required

4 page

Requirements
Must have
• i need to see template for
• 1. Home page
• 2. Page after login. People can se one or more bill to Pay and decide to see more details or to pay.
• 3. Page to Pay. Choose the desired payment method five alternative

```html
<!DOCTYPE html>
<html lang="en">
<head>
<meta charset="utf-8">
<title>zumoKet – Make Payment</title>
<link rel="stylesheet" href="https://fonts.googleapis.com/css2?family=Raleway:wght@500;600;700;800&family=Roboto:wght@400;500;700&display=swap">
<style>
:root{
  --ink:#333333;
  --muted:#555555;
  --white:#ffffff;
  --panel:rgba(247,247,247,0.95);
  --menu:rgba(40,38,36,0.86);
  --accent:#00adef;
  --border:#8a8a8a;
  --footer:#f2f2f2;
}
*{box-sizing:border-box;margin:0;padding:0}
html,body{width:1200px;height:677px;overflow:hidden}
body{position:relative;font-family:'Roboto',sans-serif;color:var(--ink);background:var(--footer)}
.hero{position:absolute;left:0;top:0;width:1200px;height:602px;
  background:
    radial-gradient(ellipse at 15% 20%,rgba(70,110,40,.55),transparent 45%),
    radial-gradient(ellipse at 60% 10%,rgba(120,150,80,.35),transparent 40%),
    linear-gradient(90deg,#3a3431 0%,#6b5d55 30%,#b9b2ac 60%,#8e8c8c 80%,#5b5b5e 100%);}
.hero::after{content:"";position:absolute;inset:0;background:linear-gradient(180deg,rgba(0,0,0,.1),rgba(0,0,0,.35))}
.brand{position:absolute;left:130px;top:13px;font-family:'Raleway',sans-serif;font-weight:700;font-size:29px;color:var(--white)}
.user{position:absolute;left:950px;top:19px;height:37px;display:flex;align-items:center}
.user-avatar{width:37px;height:37px;border-radius:50%;background:var(--white);position:relative;z-index:2;display:flex;align-items:center;justify-content:center}
.user-box{margin-left:-9px;height:33px;width:127px;border:2px solid var(--white);display:flex;align-items:center;padding-left:24px;gap:18px;color:var(--white);font-family:'Raleway',sans-serif;font-weight:700;font-size:13px}
.page-title{position:absolute;left:232px;top:115px;font-family:'Raleway',sans-serif;font-weight:800;font-size:24px;color:var(--white);letter-spacing:.2px}
.methods{position:absolute;left:232px;top:161px;width:301px;list-style:none}
.method{position:absolute;left:0;width:301px;height:50px;background:var(--menu);color:var(--white);font-family:'Raleway',sans-serif;font-weight:500;font-size:15px;display:flex;align-items:center;padding-left:26px}
.method.active{background:var(--white);color:var(--ink);border-left:3px solid var(--accent);padding-left:23px}
.method.active svg{position:absolute;right:3px;top:21px}
.payment-panel{position:absolute;left:533px;top:161px;width:435px;height:370px;background:var(--panel)}
.field{position:absolute;height:42px;border:1px solid var(--border);background:var(--white);font-size:12px;color:var(--ink);display:flex;align-items:center;padding-left:16px}
.field svg{position:absolute;right:12px}
.label{position:absolute;font-size:10px;color:var(--ink)}
.pay-button{position:absolute;left:25px;top:306px;width:400px;height:46px;background:var(--accent);color:var(--white);font-weight:700;font-size:19px;display:flex;align-items:center;justify-content:center;border:none}
.footer-note{position:absolute;left:0;top:634px;width:1200px;text-align:center;font-size:10px;color:var(--muted)}
</style>
</head>
<body>
<div class="hero" role="img" aria-label="Background photo of hands typing on a keyboard beside a plant and monitor"></div>

<div class="brand">zumoKet</div>

<div class="user">
  <div class="user-avatar">
    <svg width="14" height="15" viewBox="0 0 14 15"><circle cx="7" cy="4" r="3.6" fill="#333"/><path d="M0 15c0-4.5 3-6.5 7-6.5s7 2 7 6.5z" fill="#333"/></svg>
  </div>
  <div class="user-box">LENA
    <svg width="12" height="11" viewBox="0 0 12 11"><path d="M1 1h4v1.5H2.5v6H5V10H1z" fill="#fff"/><path d="M6 3h2.5V1L12 5.5 8.5 10V8H6z" fill="#fff"/></svg>
  </div>
</div>

<h1 class="page-title">MAKE PAYMENT</h1>

<ul class="methods">
  <li class="method" style="top:0">Pay via CashLink</li>
  <li class="method active" style="top:55px">Pay with your credit card
    <svg width="5" height="9" viewBox="0 0 5 9"><path d="M0 0l5 4.5L0 9z" fill="#00adef"/></svg></li>
  <li class="method" style="top:112px">Pay with Wire Transfer</li>
  <li class="method" style="top:169px">Pay in instalments</li>
  <li class="method" style="top:225px">Print Bulletin</li>
</ul>

<form class="payment-panel">
  <div class="field" style="left:23px;top:21px;width:397px">Card Number</div>
  <span class="label" style="left:22px;top:91px">Month of &nbsp;Expiry</span>
  <span class="label" style="left:228px;top:91px">Year of Expiry</span>
  <div class="field" style="left:23px;top:108px;width:190px;padding-left:13px">Select Month
    <svg width="9" height="5" viewBox="0 0 9 5"><path d="M0 0h9L4.5 5z" fill="#333"/></svg></div>
  <div class="field" style="left:230px;top:108px;width:190px;padding-left:13px">Select Year
    <svg width="9" height="5" viewBox="0 0 9 5"><path d="M0 0h9L4.5 5z" fill="#333"/></svg></div>
  <div class="field" style="left:23px;top:175px;width:397px">Name on Card</div>
  <div class="field" style="left:23px;top:239px;width:193px">CVV Code
    <svg width="13" height="10" viewBox="0 0 13 10"><rect x=".5" y=".5" width="12" height="9" rx="1" fill="none" stroke="#333"/><rect x="1" y="3" width="11" height="1.8" fill="#333"/><rect x="2.5" y="6.3" width="4" height="1.2" fill="#333"/></svg></div>
  <button class="pay-button" type="button">PAY $29.99</button>
</form>

<p class="footer-note">Copyrights @ 2017 All Rights Reserved</p>
</body>
</html>
```